KPT Building And Maintenance

Need a very professional looking double sided Buisiness card with all my details phone number, name, email, license number.

Target Market(s)

construction industry

Industry/Entity Type

building

Contact Information for Business Card

Name Dale Whitcombe. Email Address Info@KPTBuilding.example.au mobile number 0452918730 licence number 871406D. web site

```html
<!DOCTYPE html>
<html lang="en">
<head>
<meta charset="utf-8">
<title>KPT Building And Maintenance – Business Card</title>
<link href="https://fonts.googleapis.com/css2?family=Montserrat:wght@400;500;800&display=swap" rel="stylesheet">
<style>
  :root {
    --brand-blue: #4a9dd6;
    --brand-blue-deep: #2f6f9e;
    --ink-grey: #3d3d3f;
    --paper-white: #ffffff;
    --backdrop: #e9ebee;
  }
  * { box-sizing: border-box; margin: 0; padding: 0; }
  html, body {
    width: 1200px; height: 912px; overflow: hidden;
    background: var(--backdrop);
    font-family: "Montserrat", sans-serif;
  }
  .canvas { position: relative; width: 1200px; height: 912px; }

  .card {
    position: absolute;
    width: 600px; height: 343px;
    overflow: hidden;
    background: var(--brand-blue);
    box-shadow: 0 10px 28px rgba(0,0,0,.22);
  }
  .card--back { left: 70px; top: 90px; }
  .card--front { left: 530px; top: 480px; }

  .back-wordmark {
    position: absolute; inset: 0;
    display: flex; align-items: center; justify-content: center;
    font-weight: 800; font-size: 120px; letter-spacing: 4px;
    color: var(--brand-blue-deep);
  }

  .front-shape { position: absolute; inset: 0; }

  .front-wordmark {
    position: absolute; left: 375px; top: 58px;
    width: 200px; text-align: center;
    color: var(--ink-grey); font-weight: 800; line-height: 1;
  }
  .front-wordmark .mark-name { display: block; font-size: 68px; letter-spacing: 2px; }
  .front-wordmark .mark-sub { display: block; font-size: 27px; letter-spacing: 2px; margin-top: 6px; }

  .holder {
    position: absolute; left: 36px; top: 58px;
    color: var(--paper-white);
  }
  .holder-name { font-weight: 800; font-size: 21px; letter-spacing: 1px; }
  .holder-role { font-weight: 400; font-size: 14px; margin-top: 2px; margin-left: 14px; }

  .details {
    position: absolute; left: 60px; bottom: 32px;
    color: var(--paper-white); font-size: 14px; line-height: 1.35;
  }
  .details .licence { margin-bottom: 10px; }
  .contact-list { list-style: none; }
  .contact-list li { display: flex; align-items: center; gap: 8px; font-size: 15px; line-height: 1.45; }
  .contact-list svg { width: 13px; height: 13px; flex: none; fill: var(--paper-white); }
</style>
</head>
<body>
<main class="canvas">

  <section class="card card--back" aria-label="Card back">
    <div class="back-wordmark">KPT</div>
  </section>

  <section class="card card--front" aria-label="Card front">
    <svg class="front-shape" viewBox="0 0 600 343" aria-hidden="true">
      <path d="M 321 143 A 206 206 0 0 0 502 295" fill="none" stroke="var(--ink-grey)" stroke-width="7" stroke-linecap="round"/>
      <circle cx="520" cy="90" r="198" fill="var(--paper-white)"/>
    </svg>

    <div class="front-wordmark">
      <span class="mark-name">KPT</span>
      <span class="mark-sub">BUILDING</span>
    </div>

    <div class="holder">
      <p class="holder-name">DALE WHITCOMBE</p>
      <p class="holder-role">Director</p>
    </div>

    <div class="details">
      <p class="licence">KPT BUILDING<br>licence number 871406D.</p>
      <ul class="contact-list">
        <li>
          <svg viewBox="0 0 14 14"><path d="M4 0h6a1.5 1.5 0 0 1 1.5 1.5v11A1.5 1.5 0 0 1 10 14H4a1.5 1.5 0 0 1-1.5-1.5v-11A1.5 1.5 0 0 1 4 0zm0 2v9h6V2zm3 9.6a.8.8 0 1 0 0 1.6.8.8 0 0 0 0-1.6z"/></svg>
          045-291-8730
        </li>
        <li>
          <svg viewBox="0 0 14 14"><path d="M0 3h14v8H0zm1.2 1 5.8 4 5.8-4z"/></svg>
          Info@KPTBuilding.example.au
        </li>
        <li>
          <svg viewBox="0 0 14 14"><path d="M7 0a7 7 0 1 0 0 14A7 7 0 0 0 7 0zm0 1.3c.9 0 1.8 2 2 4.9H5c.2-2.9 1.1-4.9 2-4.9zM1.3 7.8h2.4c.1 1.7.4 3.2 1 4.2a5.7 5.7 0 0 1-3.4-4.2zm0-1.6a5.7 5.7 0 0 1 3.4-4.2c-.6 1-.9 2.5-1 4.2zm3.7 1.6h4c-.2 2.9-1.1 4.9-2 4.9s-1.8-2-2-4.9zm5.3 0h2.4a5.7 5.7 0 0 1-3.4 4.2c.6-1 .9-2.5 1-4.2zm0-1.6c-.1-1.7-.4-3.2-1-4.2a5.7 5.7 0 0 1 3.4 4.2z"/></svg>
          www.kptpartners.example.au
        </li>
      </ul>
    </div>
  </section>

</main>
</body>
</html>
```